Brochure Design Template

We need a template design so we can add and change content as required.

The size is A4 Landscape (297mm X 210mm) divided into three individual DL sections (99mm X 210mm) that have their own individual color or look. This give us the option to print as DL or have three separate services offered on on brochure.

So who are we. We are a photographic service that in Australia that offers service from commercial photography, photography training, photographic studio hire as well as a photo booth.
Our website is brimlane.net.

We are after ideas that are modern and colorful and fits the look of our logo.. Please feel free to put questions or ideas to us..
Thanks kindly..
Updates

Target Market(s)

weddings and commerical businesses

Industry/Entity Type

Landscape

Requirements
Must have
• The size is A4 Landscape (297mm X 210mm) divided into three individual DL sections (99mm X 210mm) that have their own individual color or look. This give us the option to print as DL or have three separate services offered on on brochure.

Template is for use in Adobe indesign

```html
<!DOCTYPE html>
<html lang="en">
<head>
<meta charset="utf-8">
<title>Brimlane Photographic – DL Brochure Panels</title>
<link rel="stylesheet" href="https://fonts.googleapis.com/css2?family=Cinzel:wght@600&family=Didact+Gothic&family=Roboto+Condensed:ital,wght@0,400;1,400&display=swap">
<style>
:root{
  --red:#e0252b;
  --red-dark:#b5161c;
  --ink:#3a3a3a;
  --grey:#8c8c8c;
  --paper:#ffffff;
  --paper-shade:#ececec;
  --stage:#5b5550;
}
*{margin:0;padding:0;box-sizing:border-box}
html,body{width:873px;height:1200px;overflow:hidden;background:var(--stage)}
.sheet{position:relative;width:873px;height:1200px}
.panel{position:absolute;width:254px;height:538px;overflow:hidden;
  background:linear-gradient(180deg,var(--paper) 60%,var(--paper-shade));
  font-family:"Didact Gothic",sans-serif;color:var(--ink);font-size:6.2px;line-height:1.42}
.row-front{top:59px}.row-back{top:618px}
.col-1{left:31px}.col-2{left:310px}.col-3{left:590px}
.abs{position:absolute}
.brand{position:absolute;display:flex;align-items:center;gap:6px}
.brand-dot{width:18px;height:18px;border-radius:50%;background:var(--ink)}
.brand-name{font-family:"Didact Gothic",sans-serif;font-size:20px;letter-spacing:.5px;color:var(--red)}
.brand.small .brand-dot{width:14px;height:14px}
.brand.small .brand-name{font-size:15px}
.heading{position:absolute;left:19px;font-family:"Cinzel",serif;font-weight:600;
  font-size:11px;color:var(--red);border-bottom:1px solid var(--red);padding-bottom:1px;letter-spacing:.3px}
.copy{position:absolute;left:19px;right:19px;text-align:justify}
.copy p+p{margin-top:6px}
.list{list-style:none}
.list li{position:relative;padding-left:8px;margin-top:6px}
.list li::before{content:"";position:absolute;left:0;top:2px;width:4px;height:4px;border-radius:50%;background:var(--red)}
.list b{font-weight:normal;color:#111}
.accent{color:var(--red)}
.callout{font-style:italic;color:var(--red);text-align:center;font-size:6.4px}
.photo{position:absolute}
.footer{position:absolute;left:0;bottom:0;width:254px}
.footer svg{display:block}
.footer-title{position:absolute;left:0;right:0;text-align:center;color:#fff;
  font-family:"Roboto Condensed",sans-serif;font-size:17.5px;letter-spacing:.2px}
.footer-contact{position:absolute;left:0;right:0;text-align:center;color:#fff;
  font-family:"Roboto Condensed",sans-serif;font-style:italic;font-size:11.5px}
.footer-url{position:absolute;left:0;right:0;bottom:12px;text-align:center;color:#fff;font-size:11px}
</style>
</head>
<body>
<div class="sheet">

  <!-- Front: commercial photography -->
  <section class="panel row-front col-1">
    <div class="brand" style="left:55px;top:30px"><span class="brand-dot"></span><span class="brand-name">BRIMLANE</span></div>
    <h2 class="heading" style="top:88px">Photography-Services</h2>
    <div class="copy" style="top:104px">
      <p>Brimlane Photographic Services provides unique event, corporate, portraiture, architecture and landscape photography services across New South Wales, Australia. They specialise in training, photographic tours and also have a studio space and photobooth available to hire...</p>
      <p style="padding-left:8px">Brimlane offer a wide range of professional photography services including:</p>
      <ul class="list">
        <li><b>Commercial</b> – covering corporate, staff and business promotion.</li>
        <li><b>Events</b> – including open days, sports, shows, parties and media promotions.</li>
        <li><b>Elevated Photography</b> – twenty metre photography platform to cover the aerial perspective.</li>
        <li><b>Real Estate</b> – from home owners to real estate agents to property developers and rural properties.</li>
        <li><b>Portraiture</b> – beautiful portraits are created within our two professional studios or on location.</li>
        <li><b>Landscape</b> – Architecture.</li>
        <li><b>Fine Art</b> – can be commission upon request.</li>
      </ul>
    </div>
    <div class="photo" role="img" aria-label="Photographer shooting through a camera on location" style="left:8px;top:344px;width:240px;height:104px;background:linear-gradient(120deg,#6b5440,#b98a5a 55%,#3c3530)"></div>
    <div class="footer" style="height:116px">
      <svg width="254" height="116" viewBox="0 0 254 116"><path d="M0 22 Q120 -6 254 14 L254 22 Q120 2 0 30Z" fill="#555"/><path d="M0 30 Q120 4 254 20 L254 116 L0 116Z" fill="var(--red)"/><path d="M0 44 Q130 18 254 34 L254 116 L0 116Z" fill="var(--red-dark)" opacity=".35"/></svg>
      <div class="footer-title" style="top:62px">COMMERCIAL PHOTOGRAPHY</div>
      <div class="footer-contact" style="top:86px">Contact us via email or phone 0400 318 275</div>
    </div>
  </section>

  <!-- Front: photography training -->
  <section class="panel row-front col-2">
    <div class="brand" style="left:55px;top:30px"><span class="brand-dot"></span><span class="brand-name">BRIMLANE</span></div>
    <h2 class="heading" style="top:88px">Studio Workshop</h2>
    <div class="copy" style="top:104px">
      <p>This studio workshop will unravel the mystery behind using strobe lighting within a studio environment and let you take control of studio lighting conditions.</p>
      <p class="accent">Next Course: 29th June 2013<br>Course Costs: $220</p>
      <p>This workshop is designed for those who want more from their photography and want to understand how studio lighting works. We will look at understanding how strobes work and how to use them in different lighting conditions. You get to see and use a number of accessories that are available in the market place. Once we understand the stand studio, we will then progress to a set shoot using multiple strobes and soft boxes to create unique lighting conditions. The workshop is designed to be fun, whilst providing lighting challenges within a working professional studio.</p>
    </div>
    <div class="photo" role="img" aria-label="Model in a long gown posing under studio strobes" style="left:33px;top:259px;width:187px;height:196px;background:linear-gradient(160deg,#d9d9d9,#8a8a8a 50%,#c4262a 80%,#555)"></div>
    <div class="footer" style="height:116px">
      <svg width="254" height="116" viewBox="0 0 254 116"><path d="M0 22 Q120 -6 254 14 L254 22 Q120 2 0 30Z" fill="#555"/><path d="M0 30 Q120 4 254 20 L254 116 L0 116Z" fill="var(--red)"/><path d="M0 44 Q130 18 254 34 L254 116 L0 116Z" fill="var(--red-dark)" opacity=".35"/></svg>
      <div class="footer-title" style="top:62px">PHOTOGRAPHY TRAINING</div>
      <div class="footer-contact" style="top:86px">Contact us via email or phone 0400 318 275</div>
    </div>
  </section>

  <!-- Front: photographic studio -->
  <section class="panel row-front col-3">
    <div class="brand" style="left:55px;top:30px"><span class="brand-dot"></span><span class="brand-name">BRIMLANE</span></div>
    <h2 class="heading" style="top:88px">About Us</h2>
    <div class="copy" style="top:104px">
      <p>Brimlane Photographic Services provides unique event, corporate, portraiture, architecture and landscape photography services across New South Wales, Australia. They specialise in training, photographic tours and also have a studio space and photobooth available to hire...</p>
      <p>Brimlane Photographic Services specialises in producing high-quality images and will ensure that all our shoots are relaxed, professional and trouble-free. We provide a secure and easy-to-use online store for purchasing professional print and digital products that you will treasure forever. Contact us to discuss your requirements and let us show you how we can make your event extra special.</p>
    </div>
    <div class="photo" role="img" aria-label="Studio portrait of a woman in a purple wrap" style="left:38px;top:223px;width:175px;height:193px;background:radial-gradient(circle at 55% 45%,#8a4a6a,#4a1838 45%,#1a1012)"></div>
    <div class="footer" style="height:116px">
      <svg width="254" height="116" viewBox="0 0 254 116"><path d="M0 22 Q120 -6 254 14 L254 22 Q120 2 0 30Z" fill="#555"/><path d="M0 30 Q120 4 254 20 L254 116 L0 116Z" fill="var(--red)"/><path d="M0 44 Q130 18 254 34 L254 116 L0 116Z" fill="var(--red-dark)" opacity=".35"/></svg>
      <div class="footer-title" style="top:62px">PHOTOGRAPHIC STUDIO</div>
      <div class="footer-contact" style="top:86px">Contact us via email or phone 0400 318 275</div>
    </div>
  </section>

  <!-- Back: studio hire -->
  <section class="panel row-back col-1">
    <h2 class="heading" style="top:25px">Studio-Hire</h2>
    <div class="copy" style="top:42px"><p>Brimlane has a unique fully equipped studio space that can be hired. The space is ideal for portraits that can be captured with a white seamless background or one of other eight backdrops available for use.</p></div>
    <div class="photo" role="img" aria-label="Dramatic studio portrait of a seated woman" style="left:58px;top:86px;width:136px;height:110px;background:radial-gradient(circle at 50% 40%,#a07460,#3a2620 55%,#120c0a)"></div>
    <div class="copy" style="top:210px"><p>Note: Users must provide evidence that they are trained in studio lighting or have completed a Brimlane studio course. All users will need to have completed an orientation course prior to use the facility in accordance with WHS and duty of care requirements.</p></div>
    <div class="copy" style="top:252px;text-align:left"><p>The facilities includes:<br>Three studio lights on tripods or booms<br>Lighting accessories<br>Numerous backdrops to use<br>Access to two studio spaces</p></div>
    <div class="copy" style="top:334px;right:auto;text-align:left"><p>Coffee/Tea facilities<br>Make up and<br>change room facilities</p></div>
    <div class="photo" role="img" aria-label="Make-up artist preparing a model" style="left:94px;top:304px;width:142px;height:98px;background:linear-gradient(120deg,#5a3a2a,#c39070 50%,#e8d6c6)"></div>
    <div class="brand small" style="left:19px;top:420px"><span class="brand-dot"></span><span class="brand-name">BRIMLANE</span></div>
    <div class="footer" style="height:92px">
      <svg width="254" height="92" viewBox="0 0 254 92"><path d="M0 10 Q130 24 254 8 L254 14 Q130 30 0 16Z" fill="#555"/><path d="M0 18 Q130 32 254 16 L254 92 L0 92Z" fill="var(--red)"/><path d="M0 30 Q130 44 254 28 L254 92 L0 92Z" fill="var(--red-dark)" opacity=".3"/></svg>
      <div class="footer-url">www.brimlane.net</div>
    </div>
  </section>

  <!-- Back: workshops -->
  <section class="panel row-back col-2">
    <h2 class="heading" style="top:25px">Workshops</h2>
    <div class="copy" style="top:42px">
      <p>Enrol in the most comprehensive workshops and courses for digital photography, designed for everyone from beginners to people wanting to explore new photographic styles</p>
      <p>These photography courses designed for those who are new to the digital SLR photography world and want to get professional looking images from their new camera or for people just wanting to learn more...</p>
    </div>
    <div class="photo" role="img" aria-label="Two photographers shooting a mountain lake landscape" style="left:36px;top:124px;width:182px;height:118px;background:linear-gradient(180deg,#c9cfd4,#6f7f8e 40%,#2f3a44 70%,#1b2430)"></div>
    <p class="copy callout" style="top:253px">Our workshops are a boutique experience with a maximum of<br>Only six students on our basic courses and a maximum of ten<br>N some our other workshops.</p>
    <div class="copy" style="top:296px">
      <p>Our courses includes:</p>
      <ul class="list">
        <li>Qualified Professional Teaching APG Photographer for your tuition</li>
        <li>Workbook with detailed notes</li>
        <li>Light refreshments available throughout the evening or day (includes water, tea &amp; coffee plus supper)</li>
        <li>Studio equipment for demonstrations</li>
        <li>Photographic field trips or studio workshops with comprehensive demonstrations</li>
        <li>Meals supplied for workshops with drinks at the completion of the training.</li>
      </ul>
    </div>
    <div class="brand small" style="left:74px;top:438px"><span class="brand-dot"></span><span class="brand-name">BRIMLANE</span></div>
    <div class="footer" style="height:80px">
      <svg width="254" height="80" viewBox="0 0 254 80"><path d="M0 4 Q130 14 254 2 L254 8 Q130 20 0 10Z" fill="#555"/><path d="M0 12 Q130 22 254 10 L254 80 L0 80Z" fill="var(--red)"/><path d="M0 24 Q130 34 254 22 L254 80 L0 80Z" fill="var(--red-dark)" opacity=".3"/></svg>
      <div class="footer-url">www.brimlane.net</div>
    </div>
  </section>

  <!-- Back: speedlight workshop -->
  <section class="panel row-back col-3">
    <h2 class="heading" style="top:25px">Speedlight Workshop</h2>
    <div class="copy" style="top:42px">
      <p>Speedlights...Flash! Confused, not sure how to get the most out of this bit of kit in your gear bag. Then the Speedlight Workshop will unravel the mystery behind using flash and let you take control of your lighting conditions.<br>This workshop is designed for those who have bought a flash but can't understand how to get the most from it. We will look at understanding how speedlights work and how to use them in different lighting conditions. You get to see and use a number of accessories that are available in the market place. Once we understand flash, we will then progress to a location shoot using multiple flashes to create advanced lighting conditions. The workshop is designed to be fun, whilst providing lighting challenges.</p>
      <p style="font-style:italic">Workshops are conducted over one weekend, on a Saturday &amp; Sunday from 9:00 am to 4:00pm pm daily.</p>
    </div>
    <p class="copy callout" style="top:192px;left:26px;right:auto;width:80px;text-align:right">THIS IS A BOUTIQUE EXPERIENCE WITH A MAXIMUM OF ONLY SIX STUDENTS PER COURSE...</p>
    <div class="photo" role="img" aria-label="Woman in a green gown among tree trunks, lit by flash" style="left:114px;top:192px;width:121px;height:183px;background:linear-gradient(90deg,#3a2a1e,#8a7a62 40%,#1f6b4a 60%,#4a3a2a)"></div>
    <div class="copy" style="top:258px;right:auto;width:88px"><p>No previous experience is necessary for this workshop. Its 'hands-on' practical and is designed as a fun photography course for anyone wanting to get the most from their speedlight. We explain how to use your speedlight in plain English and teach you how to take control of the lighting conditions using artificial light.</p></div>
    <p class="abs accent" style="top:390px;right:19px;text-align:right;font-size:6.4px">COURSE FEE $250<br>(Numbers are limited)</p>
    <div class="brand small" style="left:128px;top:452px"><span class="brand-dot"></span><span class="brand-name">BRIMLANE</span></div>
    <div class="footer" style="height:66px">
      <svg width="254" height="66" viewBox="0 0 254 66"><path d="M0 2 Q130 10 254 0 L254 6 Q130 16 0 8Z" fill="#555"/><path d="M0 10 Q130 18 254 8 L254 66 L0 66Z" fill="var(--red)"/><path d="M0 20 Q130 28 254 18 L254 66 L0 66Z" fill="var(--red-dark)" opacity=".3"/></svg>
      <div class="footer-url">www.brimlane.net</div>
    </div>
  </section>

</div>
</body>
</html>
```